Give Bright Oak an Online Presence!

Bright Oak Property Maintenance is an Australian Owned property maintenance company who needs a stand out online presence.

BOK maintains many buildings and sites and wants to appeal to a corporate professional market with their brand new website. BOK is essentially a handyman service offering all maintenance services to home owners, office managers, real estate agents and strata managers.

The Website:
We need a corporate website that appeals to our broader customer base (property owners, property managers, office managers) the copy is being written by a professional so use filler text for now.

Things that we want:
Home page that sets us apart and appeals to the corporate and residential market. The home page needs to not focus on either the residential or commercial market. The home page should focus on our logo and branding. We have a logo already and it is attached to the brief, please use it and try to consider the colour pallette that goes with it. Whilst we want the site to appear strong and manly it is important to remember that 95% of our customers are female so we need the site to be appealing to women. Women need to believe that we are strong, dependable and trustworthy.
We'd like a quote page and potentially also the ability to get a quote from the home page (please don't put it in if it ruins the overall feel of the home page)
An "about us" page
A contact us page
A blog that's built in (we don't want to link to an external blog)
(overall we'd expect to have 6 or 7 pages total)

The site will also need coding - we expect this to be done in a separate project but need you to consider a few things about the coding side of things.

It needs to be iPhone and iPad compatible.

We'd like you to suggest the best CMS that you would use or if you would suggest not using a CMS please let us know with your submissions.

Target Market(s)

Property owners, office managers and property managers who need maintenance on buildings (So all of them)

Industry/Entity Type

Property Maintenance

Requirements
Must have
• Our Logo
Home page
About Us
Residential
Commercial
Real Estate/Strata
Contact Us/Quote
Blog
Nice to have
• Quote form included in home page
Movement on the home page at least
Should not have
• other logos, too much colour
NO FLASH

```html
<!DOCTYPE html>
<html lang="en">
<head>
<meta charset="utf-8">
<title>Bright Oak Property Maintenance</title>
<link href="https://fonts.googleapis.com/css2?family=Lustria&family=Arimo:wght@400;700&display=swap" rel="stylesheet">
<style>
:root{
  --page-bg:#e4e4e4;
  --header:#575049;
  --brand-bg:#2f2b28;
  --nav:#2d2a27;
  --nav-line:#1d1b19;
  --nav-sep:#3c3834;
  --accent:#e07a10;
  --link:#c8620a;
  --panel:#f7f7f7;
  --white:#ffffff;
  --ink:#222222;
  --heading:#333333;
  --muted:#666666;
  --rule:#dddddd;
  --field-text:#888888;
  --footer:#2e2a26;
  --icon:#a87b5c;
  --hero-top:#d6dbe0;
  --hero-bottom:#cdc8c1;
  --portrait-a:#d9d2c8;
  --portrait-b:#f1eee9;
}
*{box-sizing:border-box;margin:0;padding:0}
html,body{width:1182px;height:1200px;overflow:hidden}
body{background:var(--page-bg);font-family:"Arimo",Arial,sans-serif;color:var(--ink);position:relative}
.site{position:absolute;left:175px;top:0;width:832px;height:1200px;background:var(--white)}

.header{position:absolute;left:0;top:0;width:832px;height:107px;background:var(--header)}
.brand{position:absolute;left:24px;top:0;width:228px;height:81px;background:var(--brand-bg);display:flex;align-items:center;gap:10px;padding-left:10px}
.brand-mark{width:52px;height:52px;background:var(--accent);flex:none}
.brand-name{font-weight:700;font-size:11px;line-height:15px;color:var(--white);text-transform:uppercase}
.search{position:absolute;left:659px;top:37px;width:165px;height:24px;background:var(--white);border:1px solid #ccc;font-size:10px;color:#999;padding:6px 8px}
.search svg{position:absolute;right:7px;top:6px}

.nav{position:absolute;left:0;top:107px;width:832px;height:59px;background:var(--nav);border-bottom:4px solid var(--nav-line)}
.nav a{position:absolute;top:0;height:55px;line-height:55px;font-family:"Lustria",Georgia,serif;font-size:12.5px;color:var(--white);text-decoration:none;text-transform:uppercase;letter-spacing:.2px}
.nav a.active{background:var(--accent);padding:0 10px}
.nav .sep{position:absolute;top:0;width:1px;height:55px;background:var(--nav-sep)}

.hero{position:absolute;left:0;top:166px;width:832px;height:354px;background:linear-gradient(180deg,var(--hero-top),var(--hero-bottom))}
.arrow{position:absolute;top:165px;width:25px;height:24px}
.arrow.prev{left:0}
.arrow.next{right:0}

.section-title{font-family:"Lustria",Georgia,serif;font-size:16px;font-weight:400;color:var(--heading);text-transform:uppercase}

.blog{position:absolute;left:0;top:520px;width:538px;height:390px;background:var(--panel)}
.blog .section-title{position:absolute;left:25px;top:28px}
.post{position:absolute;left:24px;width:500px}
.post h3{font-family:"Lustria",Georgia,serif;font-weight:400;font-size:14px;color:#444;margin-bottom:6px}
.meta{font-size:10px;color:var(--muted);margin-bottom:9px}
.meta .hl{color:var(--link)}
.meta .gap{margin-left:12px}
.post p{font-size:10px;line-height:15px;color:var(--ink)}
.divider{position:absolute;left:15px;width:508px;height:1px;background:var(--rule)}
.btn{position:absolute;height:27px;padding:0 12px;background:var(--nav);color:var(--white);font-size:10px;line-height:27px}

.quote .section-title{position:absolute;left:554px;top:548px}
.quote-rule{position:absolute;left:547px;top:569px;width:277px;height:1px;background:var(--rule)}
.field{position:absolute;left:558px;width:256px;height:31px;border:1px solid var(--rule);background:var(--white);font-size:10px;color:var(--field-text);padding:9px 10px}

.welcome .section-title{position:absolute;left:25px;top:946px}
.portrait{position:absolute;left:25px;top:980px;width:155px;height:115px;background:linear-gradient(135deg,var(--portrait-a),var(--portrait-b));border:1px solid var(--rule)}
.welcome-text{position:absolute;left:193px;top:984px;width:620px;font-size:10px;line-height:14.2px}
.welcome-text strong{display:block;margin-bottom:14px}
.welcome-text a{color:var(--link);text-decoration:none}

.footer{position:absolute;left:0;top:1145px;width:832px;height:55px;background:var(--footer);color:var(--white);font-size:10px}
.footer .copy{position:absolute;left:22px;top:23px}
.footer .follow{position:absolute;left:588px;top:24px}
.social{position:absolute;top:16px;width:22px;height:22px;background:var(--icon);border-radius:3px}
</style>
</head>
<body>
<div class="site">
  <header class="header">
    <div class="brand"><span class="brand-mark"></span><span class="brand-name">Bright Oak<br>Property Maintenance</span></div>
    <div class="search">Search site
      <svg width="10" height="10" viewBox="0 0 10 10"><circle cx="6" cy="4" r="3" fill="none" stroke="#999" stroke-width="1.2"/><line x1="4" y1="6" x2="1" y2="9" stroke="#999" stroke-width="1.4"/></svg>
    </div>
  </header>

  <nav class="nav">
    <a class="active" style="left:26px">Home</a>
    <a style="left:106px">About Us</a><span class="sep" style="left:184px"></span>
    <a style="left:201px">Residential</a><span class="sep" style="left:302px"></span>
    <a style="left:316px">Commercial</a><span class="sep" style="left:416px"></span>
    <a style="left:432px">Real Estate/Strata</a><span class="sep" style="left:583px"></span>
    <a style="left:599px">Contact Us/Quote</a><span class="sep" style="left:742px"></span>
    <a style="left:761px">Blog</a>
  </nav>

  <div class="hero" role="img" aria-label="Slideshow photo of a modern two-storey house with garages and a landscaped front garden">
    <svg class="arrow prev" viewBox="0 0 25 24"><rect width="25" height="24" fill="#222"/><path d="M15 6 L9 12 L15 18" fill="none" stroke="#fff" stroke-width="3"/></svg>
    <svg class="arrow next" viewBox="0 0 25 24"><rect width="25" height="24" fill="#222"/><path d="M10 6 L16 12 L10 18" fill="none" stroke="#fff" stroke-width="3"/></svg>
  </div>

  <section class="blog">
    <h2 class="section-title">Blog</h2>
    <article class="post" style="top:60px">
      <h3>Lorem ipsum dolor sit amet, consectetur adipiscing elit.</h3>
      <div class="meta">Posted by: <span class="hl">Admin</span><span class="gap">Date of the Post: </span><span class="hl">22/10/2012</span><span class="gap hl">25</span> Comments</div>
      <p>Aenean condimentum mattis congue. Suspendisse bibendum, purus consequat ornare fermentum, risus nisl blandit massa, non fringilla ligula massa sed purus. Donec urna nisi, fringilla eu condimentum placerat, tempus et nibh. Sed est diam, tempus nec ornare quis, ornare venenatis odio. Praesent cursus mauris eget ipsum porta in viverra magna scelerisque. Vivamus ultrices mauris eget ligula aliquam non auctor mauris sodales. Quisque in justo vitae tellus consectetur cursus id vel lorem.</p>
    </article>
    <div class="divider" style="top:194px"></div>
    <article class="post" style="top:214px">
      <h3>Donec at tortor mollis augue luctus consequat in in sapien.</h3>
      <div class="meta">Posted by: <span class="hl">Admin</span><span class="gap">Date of the Post: </span><span class="hl">22/10/2012</span><span class="gap hl">25</span> Comments</div>
      <p>Nulla vulputate, ante at blandit dapibus, enim turpis tincidunt lectus, nec accumsan diam quam sed nisl. Nulla pharetra scelerisque risus nec pretium. Suspendisse eget dui id purus bibendum vestibulum. Suspendisse a purus ut lacus posuere dapibus. Integer sed urna eu augue faucibus interdum. Fusce lacus mi, iaculis non auctor sed, eleifend ac justo.</p>
    </article>
    <div class="divider" style="top:340px"></div>
    <div class="btn" style="left:23px;top:353px">Read More</div>
  </section>

  <section class="quote">
    <h2 class="section-title">Quick Quote</h2>
    <div class="quote-rule"></div>
    <div class="field" style="top:583px">Name</div>
    <div class="field" style="top:623px">Email Address</div>
    <div class="field" style="top:664px">Phone Number</div>
    <div class="field" style="top:706px;height:146px">Comments</div>
    <div class="btn" style="left:559px;top:873px">Submit</div>
  </section>

  <section class="welcome">
    <h2 class="section-title">Welcome Our BOK Site!</h2>
    <div class="portrait" role="img" aria-label="Portrait photo of a smiling customer"></div>
    <div class="welcome-text">
      <strong>Est omnis dolore sereles massa est feipsum.</strong>
      Etoaureru moms odes necessin tatibus saepe eveniet redumsa Etoluptastusu usandaefel Itaque massa earumumelreruhic tene massatu-ram savi. Reiciendis vptatibus ass maiores alias.Asperiores repellat aurerum odes necessbsaepe eveniet utoluptates estu usanda aque. Est omnis doloresereledus etoaurerumoms odesnecessi tatibus saepe eveniet redums.Vestibulum eu varius magna. Phasellus ipsum urna, mattis at venenatis vel, mollis vel purus. Aenean nisi purus, dictum in tristique et, tristique quis libero. Praesent sed rutrum nibh. Praesent quis odio elit. Mauris lacinia auctor enim, vitae pretium sapien gravida et. Nunc egestas, diam quis facilisis fringilla, mi purus facilisis lorem, id adipiscing lectus nibh lacinia dolor. In tempus luctus tortor eget sagittis. <a>read more....</a>
    </div>
  </section>

  <footer class="footer">
    <div class="copy">© 2012 | ALL RIGHTS RESERVED | PRIVACY POLICY</div>
    <div class="follow">FOLLOW US</div>
    <span class="social" style="left:658px"></span>
    <span class="social" style="left:691px"></span>
    <span class="social" style="left:724px"></span>
    <span class="social" style="left:757px"></span>
    <span class="social" style="left:790px"></span>
  </footer>
</div>
</body>
</html>
```